Corporate Design für Steuerberatungskanzlei
Zielgruppe
Steuerberatungskanzlei
Aufgabenstellung
Es sollte hervorgehen, dass es sich um eine Steuerberatung handelt. Das Logo sollte eher simpel mit Wiedererkennungswert sein. Kreative Auseinandersetzung mit dem Firmennamen Kalvaro und der Branche.

```html
<!DOCTYPE html>
<html lang="de">
<head>
<meta charset="utf-8">
<title>Kalvaro – Geschäftsausstattung</title>
<link href="https://fonts.googleapis.com/css2?family=Montserrat:wght@600&family=Open+Sans:wght@400;600&family=Allura&display=swap" rel="stylesheet">
<style>
:root{
  --bg:#ebebeb;
  --paper:#f8f8f8;
  --navy:#0b1a8c;
  --navy-soft:#24306b;
  --green:#11882f;
  --ink:#2b2b2b;
  --muted:#777;
  --window:#e3e3e3;
  --faint:rgba(36,48,107,.12);
}
*{margin:0;padding:0;box-sizing:border-box}
html,body{width:698px;height:1200px;overflow:hidden;background:var(--bg)}
body{position:relative;font-family:"Open Sans",Arial,sans-serif;color:var(--ink)}

/* name + descriptor block */
.lockup{position:absolute;display:flex;flex-direction:column;align-items:center;line-height:1}
.lockup .brand{font-family:"Montserrat",Arial,sans-serif;font-weight:600;letter-spacing:.02em;color:var(--navy)}
.lockup .tagline{display:flex;align-items:center;gap:2px;margin-top:1.5px;font-family:"Montserrat",Arial,sans-serif;font-weight:600;letter-spacing:.06em;color:var(--green)}
.lockup .tagline::before,.lockup .tagline::after{content:"";width:6px;height:.5px;background:var(--green)}

.card{position:absolute;width:159px;height:90px;overflow:hidden;box-shadow:0 1px 3px rgba(0,0,0,.25)}
.card--front{background:var(--navy)}
.card--front .lockup{left:8px;top:36px;width:56px}
.card--front .brand{font-size:8.5px;color:#fff}
.card--front .tagline{font-size:2.6px}
.card--front .ring{position:absolute;left:96px;top:14px;width:120px;height:120px;border-radius:50%;border:9px solid #fff}
.card--back{background:var(--paper);border-bottom:3px solid var(--green)}
.card--back .studio{position:absolute;left:0;top:30px;font-size:4.6px;display:flex;align-items:center;gap:5px}
.card--back .studio::before{content:"";width:6px;height:3.5px;background:var(--green)}
.card--back .lockup{left:89px;top:39px;width:60px}
.card--back .brand{font-size:10px}
.card--back .tagline{font-size:3px}
.card--back .addr,.card--back .contact{position:absolute;top:66px;font-size:3.4px;line-height:4.1px}
.card--back .addr{left:11px}
.card--back .contact{left:99px}

.letter{position:absolute;top:392px;width:248px;height:352px;overflow:hidden;background:var(--paper);box-shadow:0 1px 3px rgba(0,0,0,.2)}
.letter .lockup{top:35px;width:48px}
.letter .brand{font-size:8.5px}
.letter .tagline{font-size:2.6px}
.letter .ring{position:absolute;left:140px;top:255px;width:130px;height:130px;border-radius:50%;border:14px solid var(--faint)}
.letter .sender{position:absolute;left:19px;top:53px;font-size:2.8px;padding-bottom:1px;border-bottom:.5px solid var(--ink)}
.recipient{position:absolute;left:28px;top:75px;font-size:3.6px;line-height:5.3px;color:var(--muted)}
.recipient strong{display:block;font-size:5.4px;line-height:8px;color:var(--ink);font-weight:600}
.date{position:absolute;right:28px;top:100px;font-size:3.6px;color:var(--muted)}
.body{position:absolute;left:28px;top:117px;width:192px;font-size:3.6px;line-height:5.4px;color:var(--muted);text-align:justify}
.body p{margin-bottom:5.4px}
.sign{position:absolute;left:28px;top:252px}
.sign .script{font-family:"Allura",cursive;font-size:10px;line-height:10px}
.sign .name{font-size:4.8px;font-weight:600}
.sign .role{font-size:3.6px;color:var(--muted)}
.fold{position:absolute;left:0;width:6px;height:.5px;background:var(--ink)}
.footer{position:absolute;left:20px;right:20px;top:330px;border-top:.7px solid var(--ink);display:flex;justify-content:space-between;padding-top:5px;font-size:2.5px;line-height:3.2px;background:transparent}
.footer div{padding-right:6px;border-right:.6px solid var(--ink)}
.footer div:last-child{border:none}

.envelope{position:absolute;left:201px;width:296px;height:153px;background:linear-gradient(135deg,#fdfdfd,#f1f1f1);box-shadow:0 1px 3px rgba(0,0,0,.2)}
.envelope--front{top:769px}
.envelope--front .lockup{left:28px;top:54px;width:48px}
.envelope--front .brand{font-size:8.5px}
.envelope--front .tagline{font-size:2.6px}
.envelope--front .window{position:absolute;left:21px;top:83px;width:117px;height:54px;border-radius:3px;background:var(--window)}
.envelope--back{top:942px;overflow:hidden}
.envelope--back svg{position:absolute;left:0;top:0}
.envelope--back .flap-name{position:absolute;left:0;right:0;top:20px;text-align:center;font-family:"Montserrat",Arial,sans-serif;font-weight:600;font-size:9px;letter-spacing:.02em;color:#fff}
</style>
</head>
<body>

<!-- business cards -->
<div class="card card--front" style="left:97px;top:67px"><span class="ring"></span><div class="lockup"><span class="brand">KALVARO</span><span class="tagline">STEUERBERATUNG</span></div></div>
<div class="card card--back" style="left:269px;top:67px">
  <span class="studio">Grafikwerkstatt</span>
  <div class="lockup"><span class="brand">KALVARO</span><span class="tagline">STEUERBERATUNG</span></div>
  <div class="addr">GRAFIKWERKSTATT<br>Ahornweg 7<br>D-90402 Nürnberg</div>
  <div class="contact">Tel: 089 / 00 00 00 - 00<br>Fax: 089 / 00 00 00 - 0000<br>Mobil: 0178 / 000 00 00<br>info@grafikwerkstatt-beispiel.de</div>
</div>
<div class="card card--front" style="left:441px;top:67px"><span class="ring"></span><div class="lockup"><span class="brand">KALVARO</span><span class="tagline">STEUERBERATUNG</span></div></div>

<div class="card card--back" style="left:97px;top:171px">
  <span class="studio">Grafikwerkstatt</span>
  <div class="lockup"><span class="brand">KALVARO</span><span class="tagline">STEUERBERATUNG</span></div>
  <div class="addr">GRAFIKWERKSTATT<br>Ahornweg 7<br>D-90402 Nürnberg</div>
  <div class="contact">Tel: 089 / 00 00 00 - 00<br>Fax: 089 / 00 00 00 - 0000<br>Mobil: 0178 / 000 00 00<br>info@grafikwerkstatt-beispiel.de</div>
</div>
<div class="card card--front" style="left:269px;top:171px"><span class="ring"></span><div class="lockup"><span class="brand">KALVARO</span><span class="tagline">STEUERBERATUNG</span></div></div>
<div class="card card--back" style="left:441px;top:171px">
  <span class="studio">Grafikwerkstatt</span>
  <div class="lockup"><span class="brand">KALVARO</span><span class="tagline">STEUERBERATUNG</span></div>
  <div class="addr">GRAFIKWERKSTATT<br>Ahornweg 7<br>D-90402 Nürnberg</div>
  <div class="contact">Tel: 089 / 00 00 00 - 00<br>Fax: 089 / 00 00 00 - 0000<br>Mobil: 0178 / 000 00 00<br>info@grafikwerkstatt-beispiel.de</div>
</div>

<div class="card card--front" style="left:97px;top:275px"><span class="ring"></span><div class="lockup"><span class="brand">KALVARO</span><span class="tagline">STEUERBERATUNG</span></div></div>
<div class="card card--back" style="left:269px;top:275px">
  <span class="studio">Grafikwerkstatt</span>
  <div class="lockup"><span class="brand">KALVARO</span><span class="tagline">STEUERBERATUNG</span></div>
  <div class="addr">GRAFIKWERKSTATT<br>Ahornweg 7<br>D-90402 Nürnberg</div>
  <div class="contact">Tel: 089 / 00 00 00 - 00<br>Fax: 089 / 00 00 00 - 0000<br>Mobil: 0178 / 000 00 00<br>info@grafikwerkstatt-beispiel.de</div>
</div>
<div class="card card--front" style="left:441px;top:275px"><span class="ring"></span><div class="lockup"><span class="brand">KALVARO</span><span class="tagline">STEUERBERATUNG</span></div></div>

<!-- letterhead, first page -->
<div class="letter" style="left:98px">
  <span class="ring"></span>
  <div class="lockup" style="left:25px"><span class="brand">KALVARO</span><span class="tagline">STEUERBERATUNG</span></div>
  <div class="sender">GRAFIKWERKSTATT &nbsp;|&nbsp; Ahornweg 7 &nbsp;|&nbsp; D-90402 Nürnberg</div>
  <div class="recipient"><strong>Name Surname</strong>Senior Executive<br>Address goes here. Street, City, Country<br>contact@yourmail.com<br>000-987-654-321</div>
  <div class="date">Date, 10 September, 2030</div>
  <div class="body">
    <p>Lorem ipsum dolor sit amet, consectetur adipisicing elit, sed do eiusmod tempor incididunt ut labore et dolore magna aliqua. Ut enim ad minim veniam, quis nostrud exercitation ullamco laboris nisi ut aliquip ex ea commodo consequat. Duis aute irure dolor in reprehenderit in voluptate velit esse cillum dolore eu fugiat nulla pariatur. Excepteur sint occaecat cupidatat non proident, sunt in culpa qui officia deserunt mollit anim id est laborum. Sed ut perspiciatis unde omnis iste natus error sit voluptatem accusantium doloremque laudantium, totam rem aperiam, eaque ipsa quae ab illo inventore veritatis et quasi architecto beatae vitae dicta sunt explicabo. Nemo enim ipsam voluptatem quia voluptas sit aspernatur aut odit aut fugit, sed quia consequuntur magni dolores eos qui ratione voluptatem sequi nesciunt. Neque porro voluptatem sequi nesciunt.</p>
    <p>Lorem ipsum dolor sit amet, consectetur adipisicing elit, sed do eiusmod tempor incididunt ut labore et dolore magna aliqua. Ut enim ad minim veniam, quis nostrud exercitation ullamco laboris nisi ut aliquip ex ea commodo consequat. Duis aute irure dolor in reprehenderit in voluptate velit esse cillum dolore eu fugiat nulla pariatur. Excepteur sint occaecat cupidatat non proident, sunt in culpa qui officia deserunt mollit anim id est laborum. Sed ut perspiciatis unde omnis iste natus error sit voluptatem accusantium doloremque laudantium, totam rem aperiam, eaque ipsa quae ab illo inventore veritatis et quasi architecto beatae vitae dicta sunt explicabo.</p>
    <p>Lorem ipsum dolor sit amet, consectetur adipisicing elit, sed do eiusmod tempor incididunt ut labore et dolore magna aliqua. Ut enim ad minim veniam, quis nostrud exercitation ullamco laboris nisi ut aliquip ex ea commodo consequat.</p>
  </div>
  <div class="sign"><div class="script">Namesurename</div><div class="name">NAME SURNAME</div><div class="role">General Manager</div></div>
  <span class="fold" style="top:125px"></span><span class="fold" style="top:176px"></span><span class="fold" style="top:250px"></span>
  <div class="footer">
    <div>Geschäftsführung:<br>Grafikwerkstatt<br>Sitz der Gesellschaft</div>
    <div>Amtsgericht Nürnberg HRB-Nr. 0000<br>USt-IdNr. DE000 000 000<br>Steuer-Nr. 000/000/00000</div>
    <div>Musterbank Süd<br>IBAN DE35 0000 0000 0000 00<br>BIC MUSTDEMMXXX</div>
    <div>Sparkasse Beispieltal<br>IBAN DE53 0000 0000 0000 00<br>BIC SPBTDEM1XXX</div>
  </div>
</div>

<!-- letterhead, following page -->
<div class="letter" style="left:354px">
  <div class="lockup" style="right:18px"><span class="brand">KALVARO</span><span class="tagline">STEUERBERATUNG</span></div>
  <div class="recipient"><strong>Name Surname</strong>Senior Executive<br>Address goes here. Street, City, Country<br>contact@yourmail.com<br>000-987-654-321</div>
  <div class="date">Date, 10 September, 2030</div>
  <div class="body">
    <p>Lorem ipsum dolor sit amet, consectetur adipisicing elit, sed do eiusmod tempor incididunt ut labore et dolore magna aliqua. Ut enim ad minim veniam, quis nostrud exercitation ullamco laboris nisi ut aliquip ex ea commodo consequat. Duis aute irure dolor in reprehenderit in voluptate velit esse cillum dolore eu fugiat nulla pariatur. Excepteur sint occaecat cupidatat non proident, sunt in culpa qui officia deserunt mollit anim id est laborum. Sed ut perspiciatis unde omnis iste natus error sit voluptatem accusantium doloremque laudantium, totam rem aperiam, eaque ipsa quae ab illo inventore veritatis et quasi architecto beatae vitae dicta sunt explicabo. Nemo enim ipsam voluptatem quia voluptas sit aspernatur aut odit aut fugit, sed quia consequuntur magni dolores eos qui ratione voluptatem sequi nesciunt. Neque porro voluptatem sequi nesciunt.</p>
    <p>Lorem ipsum dolor sit amet, consectetur adipisicing elit, sed do eiusmod tempor incididunt ut labore et dolore magna aliqua. Ut enim ad minim veniam, quis nostrud exercitation ullamco laboris nisi ut aliquip ex ea commodo consequat. Duis aute irure dolor in reprehenderit in voluptate velit esse cillum dolore eu fugiat nulla pariatur. Excepteur sint occaecat cupidatat non proident, sunt in culpa qui officia deserunt mollit anim id est laborum. Sed ut perspiciatis unde omnis iste natus error sit voluptatem accusantium doloremque laudantium, totam rem aperiam, eaque ipsa quae ab illo inventore veritatis et quasi architecto beatae vitae dicta sunt explicabo.</p>
    <p>Lorem ipsum dolor sit amet, consectetur adipisicing elit, sed do eiusmod tempor incididunt ut labore et dolore magna aliqua. Ut enim ad minim veniam, quis nostrud exercitation ullamco laboris nisi ut aliquip ex ea commodo consequat.</p>
  </div>
  <div class="sign"><div class="script">Namesurename</div><div class="name">NAME SURNAME</div><div class="role">General Manager</div></div>
  <span class="fold" style="top:113px"></span><span class="fold" style="top:164px"></span><span class="fold" style="top:238px"></span>
</div>

<!-- envelope -->
<div class="envelope envelope--front">
  <div class="lockup"><span class="brand">KALVARO</span><span class="tagline">STEUERBERATUNG</span></div>
  <div class="window"></div>
</div>
<div class="envelope envelope--back">
  <svg width="296" height="153" viewBox="0 0 296 153" aria-hidden="true">
    <path d="M0 0 H296 L280 35 Q272 46 258 46 H38 Q24 46 16 35 Z" fill="var(--navy-soft)"/>
  </svg>
  <span class="flap-name">KALVARO</span>
</div>

</body>
</html>
```